Velmora - New coded website

Current website is around 5 years old and corrupted in some ways...
I would like to refresh the design and to create a new coded website based on the current content .
Please refer to :
www.velmora-sample.com.au

Coded - Design and coding required

```html
<!DOCTYPE html>
<html lang="en">
<head>
<meta charset="utf-8">
<title>Velmora – Odours Controlled Naturally</title>
<link href="https://fonts.googleapis.com/css2?family=Poppins:ital,wght@0,400;0,500;0,600;0,700;1,600;1,700&display=swap" rel="stylesheet">
<style>
:root{
  --green:#6aab43;
  --green-dark:#4f9a3c;
  --green-light:#8cc063;
  --navy:#0c4767;
  --teal:#127a78;
  --ink:#111;
  --text:#444;
  --white:#fff;
  --grey-band:#f2f4f2;
}
*{margin:0;padding:0;box-sizing:border-box}
html,body{width:1200px;height:4464px;overflow:hidden}
body{position:relative;font-family:'Poppins',sans-serif;color:var(--ink);background:var(--white)}
.abs{position:absolute}
.btn{position:absolute;display:flex;align-items:center;justify-content:center;color:var(--white);font-size:14px;font-weight:500;border-radius:6px;background:linear-gradient(90deg,var(--green) 0%,var(--green-dark) 55%,var(--teal) 100%)}
.brand{display:flex;align-items:center;gap:10px}
.brand-dot{width:50px;height:50px;border-radius:50%;background:var(--green)}
.brand-name{font-size:30px;font-weight:500;color:var(--navy)}

/* header */
.topbar{left:0;top:0;width:1200px;height:75px;background:var(--white)}
.topbar .brand{position:absolute;left:61px;top:12px}
.contact-item{position:absolute;top:14px;display:flex;align-items:center;gap:12px}
.contact-icon{width:46px;height:46px;border-radius:50%;border:2px solid var(--green);display:flex;align-items:center;justify-content:center}
.contact-item small{display:block;font-size:11px;font-weight:600;color:var(--ink)}
.contact-item span{display:block;font-size:14px;color:var(--green)}
.quote-head{left:959px;top:16px;width:180px;height:41px;gap:10px;justify-content:flex-start;padding-left:10px;font-size:13px}
.quote-head i{width:26px;height:26px;border-radius:50%;background:var(--white)}
.mainnav{left:0;top:75px;width:1200px;height:38px;background:var(--navy)}
.mainnav a{position:absolute;top:9px;font-size:13px;color:var(--white);text-decoration:none;display:flex;align-items:center;gap:14px}
.mainnav a svg{width:10px;height:6px}

/* hero */
.hero{left:0;top:113px;width:1200px;height:565px;background:linear-gradient(180deg,#6f9d58 0%,#4d8a4a 45%,#2e6f5a 75%,#16536a 100%)}
.hero h1{position:absolute;left:0;top:106px;width:1200px;text-align:center;color:var(--white);font-size:54px;line-height:64px;font-weight:500}
.hero p{position:absolute;left:305px;top:244px;width:590px;text-align:center;color:var(--white);font-size:13px;line-height:21px}
.hero .btn{left:496px;top:336px;width:172px;height:40px}

/* about */
.about-photo{left:105px;top:707px;width:372px;height:372px;border-radius:50%;border:4px solid var(--green);background:linear-gradient(160deg,#b7c9b4 0%,#e6ebe7 45%,#7f9e72 100%)}
.about-badge{left:368px;top:972px;width:98px;height:98px;border-radius:50%;background:var(--white);display:flex;align-items:center;justify-content:center}
.about-badge i{width:78px;height:78px;border-radius:50%;background:var(--green)}
.eyebrow{left:647px;top:754px;font-size:15px;color:var(--green-dark);display:flex;align-items:center;gap:6px}
.eyebrow::after{content:"";width:40px;height:2px;background:var(--green)}
.about h2{position:absolute;left:647px;top:782px;font-size:38px;font-weight:500;color:var(--ink)}
.about p{position:absolute;left:647px;top:838px;width:495px;font-size:13px;line-height:21px;color:var(--text)}
.about .btn{left:647px;top:1018px;width:170px;height:39px}

/* products */
.products{left:0;top:1118px;width:1200px;height:730px;background:linear-gradient(180deg,#5c9a48 0%,#4a8f4a 40%,#2b7a5c 72%,#0f5469 100%)}
.section-title{position:absolute;width:1200px;left:0;text-align:center;font-size:36px;font-weight:500}
.products .section-title{top:162px;color:var(--white)}
.card{position:absolute;top:339px;width:340px;height:230px;background:var(--white);border-radius:6px 40px 6px 6px;box-shadow:6px 4px 0 var(--green)}
.card h3{position:absolute;left:0;bottom:65px;width:100%;text-align:center;font-size:19px;font-weight:600}
.card-photo{position:absolute;top:229px;width:226px;height:226px;border-radius:50%;border:3px solid var(--green-dark)}

/* testimonial */
.testi-mark{left:568px;top:1866px;width:62px;height:62px;border-radius:50%;background:var(--green)}
.testi blockquote{position:absolute;left:0;top:1942px;width:1200px;text-align:center;font-size:23px;font-weight:700;font-style:italic}
.testi p{position:absolute;left:280px;top:1984px;width:640px;text-align:center;font-size:13px;line-height:21px;color:var(--text)}
.testi .name{position:absolute;left:0;top:2105px;width:1200px;text-align:center;font-size:19px;font-weight:600;font-style:italic;color:var(--green)}
.testi .role{position:absolute;left:0;top:2137px;width:1200px;text-align:center;font-size:13px;color:var(--navy)}

/* video */
.video-band{left:0;top:2176px;width:1200px;height:520px;background:linear-gradient(180deg,#5da046 0%,#4a9246 55%,#1b5f66 74%,var(--navy) 74%,var(--navy) 100%)}
.video-band .section-title{top:154px;color:var(--white)}
.video-band .section-title em{font-style:normal;color:#9dd07a}
.video-frame{left:61px;top:2407px;width:1078px;height:485px;border:4px solid var(--green);border-radius:14px;background:linear-gradient(180deg,#dcdcd6 0%,#d5d8cf 55%,#5a9650 78%,#1f6a6c 100%)}
.play{left:562px;top:2612px;width:76px;height:76px;border-radius:50%;background:var(--white);display:flex;align-items:center;justify-content:center}

/* best */
.best .section-title{top:2952px;color:var(--ink)}
.feature-label{position:absolute;font-size:17px;font-weight:600;line-height:26px}
.feature-label.left{text-align:right;width:260px}
.feature-icon{position:absolute;width:86px;height:86px;border-radius:50%;background:var(--green);display:flex;align-items:center;justify-content:center}

/* clients */
.clients{left:0;top:3399px;width:1200px;height:208px;background:var(--grey-band)}
.clients h2{position:absolute;left:61px;top:84px;font-size:22px;font-weight:600}
.client{position:absolute;top:55px;height:98px;display:flex;align-items:center;gap:10px;background:var(--white);padding:0 14px;font-size:20px;font-weight:600;color:var(--navy)}
.client i{display:block;width:28px;height:28px;background:var(--navy)}
.client i.round{border-radius:50%}

/* contact */
.map{left:0;top:3607px;width:600px;height:496px;background:linear-gradient(135deg,#eef0ee 0%,#e4e6e5 60%,#dfe2e0 100%)}
.contact-panel{left:600px;top:3607px;width:600px;height:496px;background:var(--green)}
.contact-panel h2{position:absolute;left:40px;top:46px;font-size:36px;font-weight:600;color:var(--white)}
.contact-panel p{position:absolute;left:40px;top:100px;width:500px;font-size:12.5px;line-height:21px;color:var(--white)}
.field{position:absolute;left:40px;width:499px;height:38px;border:1px solid rgba(255,255,255,.85);border-radius:6px;color:var(--white);font-size:13px;padding:9px 18px}
.field.tall{height:88px}
.contact-panel .btn{left:47px;top:402px;width:107px;height:40px;background:var(--navy)}

/* footer */
.footer{left:0;top:4103px;width:1200px;height:327px;background:var(--navy);color:var(--white)}
.footer .brand{position:absolute;left:61px;top:86px}
.footer .brand-name{color:var(--white)}
.footer .about-text{position:absolute;left:61px;top:148px;width:250px;font-size:12.5px;line-height:21px}
.footer h4{position:absolute;top:67px;font-size:13px;font-weight:600}
.footer ul{position:absolute;left:336px;top:108px;list-style:none;font-size:12px;line-height:30px}
.footer .addr{position:absolute;left:614px;top:108px;width:240px;font-size:12px;line-height:21px;padding-left:24px}
.footer .tel{position:absolute;left:614px;top:162px;font-size:14px;padding-left:24px}
.footer .pin{position:absolute;left:0;top:2px}
.footer .field{left:890px;width:249px;border-color:rgba(255,255,255,.8)}
.footer .btn{left:890px;top:206px;width:119px;height:40px;background:var(--green)}
.copy{left:0;top:4430px;width:1200px;height:34px;background:var(--green);color:var(--white);font-size:11px;display:flex;align-items:center;justify-content:center}
</style>
</head>
<body>

<!-- header -->
<header class="abs topbar">
  <div class="brand"><i class="brand-dot"></i><span class="brand-name">Velmora</span></div>
  <div class="contact-item" style="left:506px">
    <div class="contact-icon"><svg width="20" height="20" viewBox="0 0 24 24"><path fill="#6aab43" d="M6.6 10.8a15.1 15.1 0 0 0 6.6 6.6l2.2-2.2c.3-.3.7-.4 1-.2 1.1.4 2.3.6 3.6.6.6 0 1 .4 1 1V20c0 .6-.4 1-1 1A17 17 0 0 1 3 4c0-.6.4-1 1-1h3.5c.6 0 1 .4 1 1 0 1.3.2 2.5.6 3.6.1.3 0 .7-.2 1z"/></svg></div>
    <div><small>CALL US TODAY</small><span>+61 (08) 5550 0142</span></div>
  </div>
  <div class="contact-item" style="left:735px">
    <div class="contact-icon"><svg width="20" height="16" viewBox="0 0 24 18"><rect x="1" y="1" width="22" height="16" rx="2" fill="none" stroke="#6aab43" stroke-width="2"/><path d="M2 3l10 7 10-7" fill="none" stroke="#6aab43" stroke-width="2"/></svg></div>
    <div><small>MAIL US</small><span>info@velmora-sample.com.au</span></div>
  </div>
  <a class="btn quote-head"><i></i>Request A Quote</a>
</header>
<nav class="abs mainnav">
  <a style="left:61px">Odour Control Products <svg viewBox="0 0 10 6"><path d="M0 0h10L5 6z" fill="#fff"/></svg></a>
  <a style="left:286px">How Biofiltration Works <svg viewBox="0 0 10 6"><path d="M0 0h10L5 6z" fill="#fff"/></svg></a>
  <a style="left:503px">Odour Control by Industry <svg viewBox="0 0 10 6"><path d="M0 0h10L5 6z" fill="#fff"/></svg></a>
  <a style="left:760px">Past Projects</a>
  <a style="left:903px">About Us</a>
  <a style="left:1034px">Blog</a>
</nav>

<!-- hero -->
<section class="abs hero" role="img" aria-label="Aerial photograph of a treatment facility surrounded by forest and hills, with a green tint">
  <h1>Odours Controlled<br>Naturally</h1>
  <p>Lorem Ipsum is simply dummy text of the printing and typesetting industry. Lorem Ipsum has been the industry's standard dummy text ever since the 1500s, when an unknown printer</p>
  <a class="btn">Request A Quote</a>
  <svg class="abs" style="left:0;top:440px" width="1200" height="126" viewBox="0 0 1200 126" preserveAspectRatio="none"><path d="M0 110C120 126 220 92 340 60 470 26 560 14 660 34 800 64 900 104 1030 96 1110 90 1160 72 1200 56V126H0z" fill="#fff"/></svg>
</section>

<!-- about -->
<section class="about">
  <div class="abs about-photo" role="img" aria-label="Photograph of a white cylindrical biofilter tank beside a treatment pond"></div>
  <div class="abs about-badge"><i></i></div>
  <div class="abs eyebrow">About Velmora</div>
  <h2>Odour Control Solutions</h2>
  <p>Velmora uses sustainable biotechnology to resolve odour and corrosion problems in a highly efficient, environmentally friendly and cost-effective manner. Our, products, the VelVent series of biofilters have been specifically engineered to overcome issues traditionally associated with biofiltration, such as bed compaction and uneven moisture levels, and our patented design achieves a removal rate of up to 99.9% per stage of treatment.</p>
  <a class="btn">Request A Quote</a>
</section>

<!-- products -->
<section class="abs products" role="img" aria-label="Misty green mountain landscape background">
  <svg class="abs" style="left:0;top:-1px" width="1200" height="80" viewBox="0 0 1200 80" preserveAspectRatio="none"><path d="M0 0H1200V10C1100 10 1000 0 880 8 760 18 690 70 560 76 420 82 300 60 180 54 100 50 40 60 0 70z" fill="#fff"/></svg>
  <h2 class="section-title">Odour Control Products</h2>
  <div class="card" style="left:61px"><h3>Products</h3></div>
  <div class="card" style="left:430px"><h3>Features</h3></div>
  <div class="card" style="left:799px"><h3>Past Projects</h3></div>
  <div class="card-photo" style="left:117px;background:linear-gradient(150deg,#8a8d86,#c9c7bd 50%,#6f7a68)" role="img" aria-label="Photograph of biofilter units inside a fenced compound"></div>
  <div class="card-photo" style="left:487px;background:radial-gradient(circle at 50% 55%,#cfe6c0 0%,#6fae4c 40%,#2f6a2d 100%)" role="img" aria-label="Photograph of a glass globe resting on moss"></div>
  <div class="card-photo" style="left:856px;background:linear-gradient(160deg,#b5a58d,#d9d3c6 45%,#77796f)" role="img" aria-label="Photograph of a row of biofilter tanks on a gravel site"></div>
  <svg class="abs" style="left:0;top:646px" width="1200" height="85" viewBox="0 0 1200 85" preserveAspectRatio="none"><path d="M0 60C140 30 260 20 380 34 520 52 640 82 780 70 920 58 1040 16 1200 6V85H0z" fill="#fff"/></svg>
</section>

<!-- testimonial -->
<section class="testi">
  <div class="abs testi-mark"></div>
  <blockquote>As soon as the system was started, the smell disappeared!</blockquote>
  <p>Velmora uses sustainable biotechnology to resolve odour and corrosion problems in a highly efficient, environmentally friendly and cost-effective manner. Our, products, the VelVent series of biofilters have been specifically engineered to overcome issues traditionally associated with biofiltration, such as bed compaction and uneven moisture levels, and our patented design achieves a removal rate of up to 99.9% per stage of treatment.</p>
  <div class="name">Maya Thornton</div>
  <div class="role">Nearby resident to Elm Creek Wastewater Pump Station</div>
</section>

<!-- video -->
<section class="abs video-band">
  <svg class="abs" style="left:0;top:-1px" width="1200" height="90" viewBox="0 0 1200 90" preserveAspectRatio="none"><path d="M0 0H1200V80C1100 86 1010 60 900 40 790 20 700 34 600 50 480 68 380 46 260 22 170 6 80 18 0 40z" fill="#fff"/></svg>
  <h2 class="section-title">Watch Our <em>Video</em></h2>
</section>
<div class="abs video-frame" role="img" aria-label="Video thumbnail illustration of two biofilter tanks among trees with gauge, savings and recycling icons"></div>
<div class="abs play"><svg width="28" height="30" viewBox="0 0 28 30"><path d="M4 2l22 13L4 28z" fill="#0c4767"/></svg></div>

<!-- what makes us the best -->
<section class="best">
  <h2 class="section-title">What makes us the best?</h2>
  <svg class="abs" style="left:420px;top:3030px" width="360" height="300" viewBox="0 0 360 300">
    <path d="M40 60A165 165 0 0 0 40 240" fill="none" stroke="#0c4767" stroke-width="2"/>
    <path d="M320 60A165 165 0 0 1 320 240" fill="none" stroke="#0c4767" stroke-width="2"/>
    <path d="M86 20A165 165 0 0 1 274 20" fill="none" stroke="#0c4767" stroke-width="2"/>
    <path d="M86 280A165 165 0 0 0 274 280" fill="none" stroke="#0c4767" stroke-width="2"/>
    <circle cx="180" cy="150" r="128" fill="#6aab43"/>
    <circle cx="29" cy="65" r="4" fill="#0c4767"/><circle cx="29" cy="220" r="4" fill="#0c4767"/>
    <circle cx="331" cy="65" r="4" fill="#0c4767"/><circle cx="331" cy="222" r="4" fill="#0c4767"/>
  </svg>
  <div class="feature-label left" style="left:57px;top:3074px">Biological &amp; Sustainable<br>technology</div>
  <div class="feature-label left" style="left:57px;top:3226px">Efficient maintenance<br>cost</div>
  <div class="feature-label" style="left:877px;top:3080px">Eco Friendly</div>
  <div class="feature-label" style="left:877px;top:3240px">100% Australian Owned</div>
  <div class="feature-icon" style="left:347px;top:3052px"><svg width="44" height="44" viewBox="0 0 44 44" fill="none" stroke="#fff" stroke-width="2"><circle cx="22" cy="16" r="9"/><path d="M22 25v14M14 33l8-4 8 4"/></svg></div>
  <div class="feature-icon" style="left:347px;top:3203px"><svg width="44" height="44" viewBox="0 0 44 44" fill="none" stroke="#fff" stroke-width="2"><circle cx="22" cy="22" r="8"/><circle cx="22" cy="22" r="16" stroke-dasharray="5 4"/></svg></div>
  <div class="feature-icon" style="left:760px;top:3052px"><svg width="44" height="44" viewBox="0 0 44 44" fill="none" stroke="#fff" stroke-width="2"><path d="M10 34C10 18 22 10 34 10 34 24 26 34 10 34z"/><path d="M10 34l16-16"/></svg></div>
  <div class="feature-icon" style="left:760px;top:3208px"><svg width="44" height="44" viewBox="0 0 44 44" fill="none" stroke="#fff" stroke-width="2"><rect x="8" y="8" width="28" height="28"/><circle cx="17" cy="18" r="3"/><circle cx="27" cy="26" r="3"/></svg></div>
</section>

<!-- clients -->
<section class="abs clients">
  <h2>Our Happy Clients</h2>
  <svg class="abs" style="left:304px;top:92px" width="14" height="26" viewBox="0 0 14 26"><path d="M12 2L2 13l10 11" fill="none" stroke="#333" stroke-width="2"/></svg>
  <div class="client" style="left:340px">Coastline City</div>
  <div class="client" style="left:556px"><i></i>Northfield Region</div>
  <div class="client" style="left:784px;padding:0 10px"><i class="round"></i>Ridgeway</div>
  <div class="client" style="left:938px">Tidewell Water</div>
  <svg class="abs" style="left:1127px;top:92px" width="14" height="26" viewBox="0 0 14 26"><path d="M2 2l10 11L2 24" fill="none" stroke="#6aab43" stroke-width="2"/></svg>
</section>

<!-- contact -->
<div class="abs map" role="img" aria-label="Street map showing the office location marked with a red pin"></div>
<section class="abs contact-panel">
  <h2>Get In Touch</h2>
  <p>If you have any queries regarding out products, please do not hesitate to contact us</p>
  <div class="field" style="top:154px">Your Name*</div>
  <div class="field" style="top:201px">E-mail Adress*</div>
  <div class="field" style="top:246px">Phone No.*</div>
  <div class="field tall" style="top:294px">Massage*</div>
  <a class="btn">Submit</a>
</section>

<!-- footer -->
<footer class="abs footer">
  <div class="brand"><i class="brand-dot"></i><span class="brand-name">Velmora</span></div>
  <p class="about-text">Velmora uses sustainable biotechnology to resolve odour and corrosion problems in a highly efficient, environmentally friendly and cost-effective manner.</p>
  <h4 style="left:336px">SITE MAP:</h4>
  <ul>
    <li>Odour Control Products</li><li>How Biofiltration Works</li><li>Odour Control by Industry</li><li>Past Projects</li><li>About Us</li><li>Blog</li>
  </ul>
  <h4 style="left:614px">CONTACT US:</h4>
  <div class="addr"><svg class="pin" width="12" height="16" viewBox="0 0 12 16"><path d="M6 0a6 6 0 0 1 6 6c0 4-6 10-6 10S0 10 0 6a6 6 0 0 1 6-6z" fill="#6aab43"/><circle cx="6" cy="6" r="2" fill="#0c4767"/></svg>14 Harbourne Way, Kelvale WA 6099, Australia</div>
  <div class="tel"><svg class="pin" width="14" height="14" viewBox="0 0 24 24"><path fill="#6aab43" d="M6.6 10.8a15.1 15.1 0 0 0 6.6 6.6l2.2-2.2c.3-.3.7-.4 1-.2 1.1.4 2.3.6 3.6.6.6 0 1 .4 1 1V20c0 .6-.4 1-1 1A17 17 0 0 1 3 4c0-.6.4-1 1-1h3.5c.6 0 1 .4 1 1 0 1.3.2 2.5.6 3.6.1.3 0 .7-.2 1z"/></svg>+61 (08) 5550 0142</div>
  <h4 style="left:890px">SUBSCRIBE TO OUR NEWSLETTER</h4>
  <div class="field" style="top:107px">Your Name*</div>
  <div class="field" style="top:154px">E-mail Adress*</div>
  <a class="btn">Subscribe</a>
</footer>
<div class="abs copy">© 2023 Velmora. All Right Reserved.</div>

</body>
</html>
```